QUORLANET - IT SERVICE PROVIDERS - TriFold Flyer

Looking for Exclusive Professional look TriFold Flyer (A4) to tell:
- what we do?
- Why choose us?
- Our Services
- Our Products
- Address and Contact Detail
From Designer:
=================
Look and Feel
Graphics - Icons - Shapes - Amazing Layouts - Exclusive Fonts.
All the content will be provided.
Please send your portfolio to check..
Reason: till now no one has send there designs - have to extend to get the designs...
If no one interested to give - then i need to ask a refund... thanx
Those who accepted my project - plz let me know your delivery dates...
and about content - plz mention the Titles which i have mentioned in Brief and put Lipsum text, i will replace them...
What i m looking is Awesome Layout and Design - Using Shapes / Graphics / Fonts... content u put lipsum content and more content you will get it from www.tenvoramix.com...
About services and other stuff.... thanx
Reason: not even 4 designers have submitted there design out of 13 acceptance.
Kindly send me the best design so as to give lots of projects...
Reason: Looking for more creative and unique design
Target Market(s)
Dubai and GCC
IT comsultants
IT Service Providers
Advertising Agencies
Software Development Cos.
Industry/Entity Type
It Professional
Look and feel

```html
<!DOCTYPE html>
<html lang="en">
<head>
<meta charset="utf-8">
<title>QUORLANET – Tri-Fold Flyer</title>
<link rel="stylesheet" href="https://fonts.googleapis.com/css2?family=Source+Sans+3:ital,wght@0,400;0,600;0,700;1,700&family=Archivo:wght@700;800&display=swap">
<style>
  :root {
    --panel-grey: #8f9399;
    --panel-grey-light: #a3a7ac;
    --navy: #1b2d57;
    --navy-deep: #17284d;
    --royal-blue: #1f56a7;
    --wine: #6b1416;
    --ink: #141414;
    --white: #ffffff;
    --photo-light: #c9d3de;
    --photo-mid: #7d8792;
    --photo-dark: #3a3e58;
  }
  * { box-sizing: border-box; margin: 0; padding: 0; }
  html, body { width: 1200px; height: 848px; overflow: hidden; background: #ffffff; }
  .flyer {
    position: relative; width: 1169px; height: 826px;
    transform: scale(1.0265); transform-origin: 0 0;
    overflow: hidden;
    font-family: "Source Sans 3", "Myriad Pro", sans-serif; color: var(--white);
  }
  .backdrop { position: absolute; inset: 0; width: 1169px; height: 826px; }

  .panel-title {
    position: absolute; top: 24px; width: 389px; text-align: center;
    font-family: "Archivo", Arial, sans-serif; font-weight: 700; font-size: 24px;
    letter-spacing: 0.3px; line-height: 30px;
  }
  .section-label {
    position: absolute; height: 31px; line-height: 31px; padding-left: 36px;
    font-size: 12px; text-transform: uppercase; letter-spacing: 0.1px;
  }
  .section-label--dark { background: linear-gradient(90deg, rgba(20,20,20,0) 0%, #1a1a1a 30%, #141414 100%); }
  .section-label--wine { background: linear-gradient(90deg, #3a0a0b 0%, var(--wine) 35%, var(--wine) 100%); }
  .section-label--band { background: linear-gradient(90deg, #2a0708 0%, #161616 35%, #141414 100%); }

  .copy {
    position: absolute; width: 318px;
    font-size: 11.6px; line-height: 19.5px; text-align: justify; hyphens: none;
  }
  .copy p + p { margin-top: 19.5px; }
  .copy--tight p + p { margin-top: 0; }

  .brand { position: absolute; left: 98px; top: 726px; width: 192px; text-align: center; }
  .brand-name {
    font-family: "Archivo", Arial, sans-serif; font-weight: 800; font-size: 30px;
    line-height: 30px; letter-spacing: 0.5px; color: var(--white);
  }
  .brand-tagline {
    font-size: 8px; letter-spacing: 3.4px; line-height: 12px; margin-top: 2px;
    border-bottom: 1px dotted rgba(255,255,255,0.7); padding-bottom: 2px;
  }
  .brand-url { font-size: 7.5px; letter-spacing: 3.2px; line-height: 12px; margin-top: 1px; }

  .service-photo { position: absolute; left: 860px; width: 210px; }
  .service-photo--software { top: 362px; height: 157px; background: linear-gradient(160deg, #eef2f6 0%, var(--photo-light) 45%, #8d9aa8 100%); }
  .service-photo--it { top: 537px; height: 80px; background: linear-gradient(100deg, #9aa1a8 0%, var(--photo-mid) 50%, #4d545c 100%); }
  .service-photo--app { top: 634px; height: 101px; background: linear-gradient(120deg, #2c3154 0%, var(--photo-dark) 50%, #25294a 100%); }
  .service-tag {
    position: absolute; left: 0; bottom: 0; height: 19px; padding: 0 9px 0 10px;
    background: var(--ink); font-weight: 700; font-style: italic; font-size: 15px; line-height: 19px;
  }
</style>
</head>
<body>
<main class="flyer">
  <svg class="backdrop" viewBox="0 0 1169 826" aria-hidden="true">
    <defs>
      <linearGradient id="fade-wine" x1="0" x2="1" y1="0" y2="0">
        <stop offset="0" stop-color="#1b0a0a"/><stop offset="0.5" stop-color="#6b1416"/><stop offset="1" stop-color="#6b1416"/>
      </linearGradient>
      <linearGradient id="grey-right" x1="0" x2="1" y1="0" y2="1">
        <stop offset="0" stop-color="#9ea2a7"/><stop offset="1" stop-color="#8c9096"/>
      </linearGradient>
      <linearGradient id="card-sheen" x1="0" x2="0" y1="0" y2="1">
        <stop offset="0" stop-color="#8e9297"/><stop offset="0.2" stop-color="#c9ccd0"/><stop offset="1" stop-color="#a9adb2"/>
      </linearGradient>
      <linearGradient id="title-rule" x1="0" x2="1">
        <stop offset="0" stop-color="#fff" stop-opacity="0"/><stop offset="0.5" stop-color="#fff" stop-opacity="0.55"/><stop offset="1" stop-color="#fff" stop-opacity="0"/>
      </linearGradient>
    </defs>
    <!-- left panel -->
    <rect x="0" y="0" width="389" height="826" fill="var(--panel-grey)"/>
    <polygon points="0,625 200,535 389,600 389,826 0,826" fill="url(#fade-wine)"/>
    <polygon points="0,655 200,571 389,650 389,826 0,826" fill="var(--navy-deep)"/>
    <polygon points="0,690 200,606 389,690 389,826 0,826" fill="var(--royal-blue)"/>
    <!-- middle panel -->
    <rect x="389" y="0" width="390" height="826" fill="var(--navy)"/>
    <polygon points="389,600 440,622 779,622 779,660 389,660" fill="var(--wine)"/>
    <!-- right panel -->
    <rect x="779" y="0" width="390" height="826" fill="url(#grey-right)"/>
    <polygon points="779,470 1169,675 1169,826 779,826" fill="var(--navy)"/>
    <polygon points="779,492 1169,700 1169,826 779,826" fill="#161616"/>
    <polygon points="850,290 1080,265 1080,750 850,750" fill="url(#card-sheen)"/>
    <polygon points="1040,735 1080,720 1080,750 1050,752" fill="#d6d8db"/>
    <!-- title rules -->
    <rect x="40" y="60" width="310" height="2" fill="url(#title-rule)"/>
    <rect x="800" y="60" width="350" height="2" fill="url(#title-rule)"/>
    <!-- label notches -->
    <circle cx="0" cy="85" r="15" fill="#c4c7cb"/>
    <circle cx="0" cy="324" r="15" fill="#c4c7cb"/>
    <circle cx="390" cy="85" r="15" fill="#8a1a1c"/>
    <circle cx="390" cy="323" r="15" fill="#8a1a1c"/>
    <circle cx="779" cy="85" r="15" fill="#c4c7cb"/>
    <circle cx="779" cy="321" r="15" fill="#c4c7cb"/>
  </svg>

  <!-- left panel -->
  <h2 class="panel-title" style="left:0;">LOREM IPSUM DOLOR</h2>
  <div class="section-label section-label--dark" style="left:0;top:70px;width:305px;">Lorem ipsum dolor sit amet</div>
  <div class="copy" style="left:36px;top:116px;">
    <p>Lorem ipsum dolor sit amet, consectetuer adipiscing elit. Suspendisse felis. Aliquam pretium risus quis sem. Praesent lobortis tortor eget est. Proin est ligula, molestie eu, nonummy vitae, dictum non, arcu. Quisque pulvinar iaculis libero.</p>
    <p>Mauris accumsan fringilla metus. Vivamus rutrum ornare ipsum. In ornare varius massa. senectus et netus et malesuada fames ac turpis egestas.</p>
  </div>
  <div class="section-label section-label--dark" style="left:0;top:309px;width:305px;">Lorem ipsum dolor sit amet</div>
  <div class="copy" style="left:36px;top:354px;">
    <p>Lorem ipsum dolor sit amet, consectetuer adipiscing elit. Suspendisse felis. Aliquam pretium risus quis sem. Praesent lobortis tortor eget est. Proin est ligula, molestie eu, nonummy vitae, dictum non, arcu. Quisque pulvinar iaculis libero.</p>
    <p>Mauris accumsan fringilla metus. Vivamus rutrum ornare ipsum. In ornare varius massa. senectus et netus et malesuada fames ac turpis egestas.</p>
  </div>
  <div class="brand">
    <div class="brand-name">QUORLANET</div>
    <div class="brand-tagline">IT SOLUTION PROVIDERS</div>
    <div class="brand-url">www.tenvoramix.com</div>
  </div>

  <!-- middle panel -->
  <h2 class="panel-title" style="left:389px;">ONLINE SERVICE</h2>
  <div class="section-label section-label--wine" style="left:389px;top:69px;width:268px;">Lorem ipsum dolor sit amet</div>
  <div class="copy" style="left:425px;top:114px;">
    <p>Lorem ipsum dolor sit amet, consectetuer adipiscing elit. Suspendisse felis. Aliquam pretium risus quis sem. Praesent lobortis tortor eget est. Proin est ligula, molestie eu, nonummy vitae, dictum non, arcu. Quisque pulvinar iaculis libero.</p>
    <p>Mauris accumsan fringilla metus. Vivamus rutrum ornare ipsum. In ornare varius massa. senectus et netus et malesuada fames ac turpis egestas.</p>
  </div>
  <div class="section-label section-label--wine" style="left:389px;top:307px;width:264px;">Lorem ipsum dolor sit amet</div>
  <div class="copy" style="left:425px;top:352px;">
    <p>Lorem ipsum dolor sit amet, consectetuer adipiscing elit. Suspendisse felis. Aliquam pretium risus quis sem. Praesent lobortis tortor eget est. Proin est ligula, molestie eu, nonummy vitae, dictum non, arcu. Quisque pulvinar iaculis libero.</p>
    <p>Mauris accumsan fringilla metus. Vivamus rutrum ornare ipsum. In ornare varius massa. senectus et netus et malesuada fames ac turpis egestas.</p>
    <p>Mauris accumsan fringilla metus. Vivamus rutrum ornare ipsum. In ornare varius massa. senectus et netus et malesuada fames ac turpis egestas.</p>
  </div>
  <div class="section-label section-label--band" style="left:389px;top:623px;width:390px;height:37px;line-height:33px;">Lorem ipsum dolor sit amet</div>
  <div class="copy" style="left:425px;top:678px;">
    <p>Lorem ipsum dolor sit amet, consectetuer adipiscing elit. Suspendisse felis. Aliquam pretium risus quis sem. Praesent lobortis tortor eget est. Proin est ligula, molestie eu, nonummy vitae, dictum non, arcu. Quisque pulvinar iaculis libero.</p>
  </div>

  <!-- right panel -->
  <h2 class="panel-title" style="left:779px;">OFFLINE SERVICE</h2>
  <div class="section-label section-label--dark" style="left:779px;top:69px;width:271px;">Lorem ipsum dolor sit amet</div>
  <div class="copy copy--tight" style="left:816px;top:114px;">
    <p>Lorem ipsum dolor sit amet, consectetuer adipiscing elit. Suspendisse felis. Aliquam pretium risus quis sem. Praesent lobortis tortor eget est. Proin est ligula, molestie eu, nonummy vitae, dictum non, arcu. Quisque pulvinar iaculis libero.</p>
    <p>Mauris accumsan fringilla metus. Vivamus rutrum ornare ipsum. In ornare varius massa. senectus et netus et malesuada fames ac turpis egestas.</p>
  </div>

  <div class="service-photo service-photo--software" role="img" aria-label="Photo of a hand typing on a laptop keyboard">
    <span class="service-tag">Software Solution</span>
  </div>
  <div class="service-photo service-photo--it" role="img" aria-label="Photo of a technician working on server hardware">
    <span class="service-tag">IT Solution</span>
  </div>
  <div class="service-photo service-photo--app" role="img" aria-label="Photo of tablets and phones showing reading apps">
    <span class="service-tag">App Solution</span>
  </div>
</main>
</body>
</html>
```